Hockey Sponsorship Proposal

We are looking for a sponsorship proposal design for an apparel company to supply our hockey camps with jerseys and apparel. We want to use lots of visuals so potential business partners can see the exposure and publicity their company could get by working with us. We would like the primary colors to be red, black and white. We have attached a bunch of images but not all need to be used. We would like to see a mix of images with adult players and youth players where appropriate. Although I have provided a rough outline for the information on the powerpoint the text and images can be displayed however you would like.

Here is a link to some proposals to give you an idea of what we are looking for
https://www.glimmerstack.co.uk/item/571204839265104937/

Target Market(s)

Athletic Apparel Companies

Industry/Entity Type

It Company

Requirements
Must have
• Please note this should be suitable for web as the proposal will be emailed. This is NOT for print.
Nice to have
• I would like the first page to have a full image as the backdrop with the text over top if possible.

```html
<!DOCTYPE html>
<html lang="en">
<head>
<meta charset="utf-8">
<title>Garrett's Camps – Sponsorship Proposal</title>
<link href="https://fonts.googleapis.com/css2?family=Fjalla+One&family=Fira+Sans:wght@600&display=swap" rel="stylesheet">
<style>
  :root {
    --page-bg: #e4e4e4;
    --panel-black: #000000;
    --accent-red: #e2252a;
    --card-grey: #e1e1e1;
    --ink: #111111;
    --white: #ffffff;
    --row-line: #ffffff;
  }
  * { box-sizing: border-box; margin: 0; padding: 0; }
  html, body { width: 1078px; height: 1200px; overflow: hidden; }
  body {
    background: var(--page-bg);
    position: relative;
    font-family: "Fira Sans", Arial, sans-serif;
    font-weight: 600;
    color: var(--ink);
  }
  .panel {
    position: absolute;
    left: 35px;
    width: 1009px;
    background: var(--panel-black);
    box-shadow: 0 4px 10px rgba(0,0,0,0.35);
    overflow: hidden;
  }
  .panel--about { top: 22px; height: 568px; }
  .panel--service { top: 604px; height: 566px; }

  .panel-title {
    position: absolute;
    left: 0; right: 0;
    text-align: center;
    font-family: "Fjalla One", "Oswald", sans-serif;
    font-weight: 400;
    font-size: 50px;
    letter-spacing: 3px;
    color: var(--white);
    line-height: 1;
    z-index: 2;
  }
  .panel-title .highlight { color: var(--accent-red); }
  .panel--about .panel-title { top: 40px; }
  .panel--service .panel-title { top: 40px; }

  .camp-card {
    position: absolute;
    top: 125px;
    width: 296px;
    height: 403px;
    background: var(--card-grey);
  }
  .camp-card:nth-of-type(1) { left: 36px; }
  .camp-card:nth-of-type(2) { left: 357px; }
  .camp-card:nth-of-type(3) { left: 678px; }
  .camp-card__head {
    height: 97px;
    background: var(--accent-red);
    color: var(--white);
    font-family: "Fjalla One", "Oswald", sans-serif;
    font-size: 33px;
    letter-spacing: 0.5px;
    display: flex;
    align-items: center;
    justify-content: center;
  }
  .camp-card__body {
    padding: 20px 14px 0;
    text-align: center;
    font-size: 17px;
    line-height: 21.5px;
  }
  .camp-card__body p + p { margin-top: 21px; }

  .player-photo {
    position: absolute;
    z-index: 0;
  }
  .player-photo--left {
    left: 0; top: 0; width: 340px; height: 130px;
    background: radial-gradient(ellipse at 55% 45%, #5a5a5a 0%, #2c2c2c 55%, #000 100%);
  }
  .player-photo--right {
    right: 0; top: 0; width: 300px; height: 310px;
    background: radial-gradient(ellipse at 55% 40%, #5c5c5c 0%, #2a2a2a 55%, #000 100%);
  }

  .requirements {
    position: absolute;
    left: 42px;
    top: 128px;
    width: 934px;
    border-collapse: collapse;
    z-index: 2;
    table-layout: fixed;
  }
  .requirements th {
    height: 62px;
    background: var(--accent-red);
    color: var(--white);
    font-family: "Fjalla One", "Oswald", sans-serif;
    font-weight: 400;
    font-size: 27px;
    border-left: 2px solid var(--row-line);
  }
  .requirements td {
    height: 49px;
    background: var(--card-grey);
    text-align: center;
    font-size: 16px;
    border-top: 2px solid var(--row-line);
    border-left: 2px solid var(--row-line);
  }
  .requirements th:first-child, .requirements td:first-child { border-left: none; }
  .col-event { width: 173px; }
  .col-item { width: 500px; }
  .col-pieces { width: 102px; }
  .col-timeline { width: 159px; }
</style>
</head>
<body>

<section class="panel panel--about">
  <h1 class="panel-title">ABOUT <span class="highlight">GARRETT’S CAMPS</span></h1>

  <article class="camp-card">
    <h2 class="camp-card__head">ASHFORD PRO CAMP</h2>
    <div class="camp-card__body">
      <p>Held annually in August in Naples, Florida</p>
      <p>2017 camp featured 44 PHL players</p>
      <p>Participants included Aldo Marchetti, Pierce Kennard, Jonah Eckert, Cyril Garneau and many more</p>
    </div>
  </article>

  <article class="camp-card">
    <h2 class="camp-card__head">ASHFORD SUPER 64</h2>
    <div class="camp-card__body">
      <p>Garrett’s premiere youth hockey event</p>
      <p>Elite camp featuring 64 of the best players in North America across several age groups</p>
      <p>Super 64 Camps held annually in Vancouver &amp; Toronto</p>
      <p>Servicing over 400 top youth hockey players</p>
    </div>
  </article>

  <article class="camp-card">
    <h2 class="camp-card__head">ASHFORD FESTIVAL</h2>
    <div class="camp-card__body">
      <p>Youth camp for players of all skill levels</p>
      <p>Camps located in various cities around North America</p>
      <p>Servicing over 500 youth hockey players</p>
    </div>
  </article>
</section>

<section class="panel panel--service">
  <div class="player-photo player-photo--left" role="img" aria-label="Black and white photo of a hockey player in helmet and jersey"></div>
  <div class="player-photo player-photo--right" role="img" aria-label="Black and white photo of a hockey player wearing a visor helmet"></div>

  <h1 class="panel-title">SERVICE <span class="highlight">REQUIREMENTS</span></h1>

  <table class="requirements">
    <colgroup>
      <col class="col-event"><col class="col-item"><col class="col-pieces"><col class="col-timeline">
    </colgroup>
    <thead>
      <tr><th>EVENT</th><th>ITEM</th><th>PIECES</th><th>TIMELINE</th></tr>
    </thead>
    <tbody>
      <tr><td>PHL Camp</td><td>Uniform (jersey/sock/pant shell)</td><td>50</td><td>Summer 2018</td></tr>
      <tr><td>PHL Camp</td><td>Apparel (some of t-shirt, shorts, hoodie, track suit, hat, toque)</td><td>50</td><td>Summer 2018</td></tr>
      <tr><td>Ashford Super 64</td><td>Uniform (jersey/sock/pant shell)</td><td>400</td><td>Spring 2018</td></tr>
      <tr><td>Ashford Super 64</td><td>Apparel (some of t-shirt, shorts, hoodie, track suit, hat, toque)</td><td>400</td><td>Spring 2018</td></tr>
      <tr><td>Ashford Festival</td><td>Uniform (jersey/sock/pant shell)</td><td>400</td><td>Spring 2018</td></tr>
      <tr><td>Ashford Festival</td><td>Apparel (some of t-shirt, shorts, hoodie, track suit, hat, toque)</td><td>400</td><td>Spring 2018</td></tr>
      <tr><td>Travel Team</td><td>Uniform (jersey/sock/pant shell)</td><td>20</td><td>Fall 2018</td></tr>
    </tbody>
  </table>
</section>

</body>
</html>
```